New Website Design for Rides for Heroes.org - A Site for People to Donate Cars to War / Disabled Ve

Current site: www.ridesforheroes.org; Look at these sites for ideas: bikez2tots.org; gearsforhopes.org; www.autosformarines.org; www.trucksforsoldiers.org

Industry/Entity Type

Charity

Coding

Coded - Design and coding required

Number of Pages Required

1 page

Requirements
Must have
• n/a
Nice to have
• n/a
Should not have
• n/a

```html
<!DOCTYPE html>
<html lang="en">
<head>
<meta charset="utf-8">
<title>Rides for Heroes – Donate Your Car</title>
<link rel="stylesheet" href="https://fonts.googleapis.com/css2?family=Montserrat:wght@600;700;800&family=Open+Sans:wght@400;600;700&display=swap">
<style>
:root{
  --page:#e9e9e9;
  --navy:#13287a;
  --navy-deep:#0c1f63;
  --nav:#1b3585;
  --royal:#2d4a9a;
  --red:#e3161d;
  --ink:#111;
  --white:#fff;
  --field:#f1f2f5;
  --line:#8a8f99;
}
*{box-sizing:border-box;margin:0;padding:0}
html,body{width:1200px;height:2341px;overflow:hidden}
body{background:var(--page);font-family:"Open Sans",Arial,sans-serif;color:var(--ink)}
.site{position:absolute;left:16px;top:16px;width:1168px;background:var(--white)}
.heading{font-family:"Montserrat",Arial,sans-serif}

/* header */
.masthead{height:149px;position:relative;background:linear-gradient(100deg,#1d2b55 0%,#3a4a72 35%,#8d93a8 60%,#c9c5cc 78%,#a3313c 100%);color:var(--white)}
.brand{position:absolute;left:50px;top:48px;display:flex;align-items:center;gap:12px}
.brand-dot{width:40px;height:40px;border-radius:50%;background:var(--red)}
.brand-name{font-family:"Montserrat",Arial,sans-serif;font-weight:800;font-size:30px;color:var(--white);text-transform:uppercase;letter-spacing:.5px}
.hotline{position:absolute;right:22px;top:28px;text-align:center;font-family:"Montserrat",Arial,sans-serif;font-weight:700;line-height:1.05}
.hotline .a{font-size:21px}
.hotline .b{font-size:30px}
.hotline .c{font-size:19px}

.mainnav{height:50px;background:var(--nav);display:flex;justify-content:center;gap:50px;align-items:center}
.mainnav a{color:var(--white);text-decoration:none;font-family:"Montserrat",Arial,sans-serif;font-weight:700;font-size:20px}

/* hero */
.hero{height:576px;position:relative;background:linear-gradient(160deg,#1a2c63 0%,#41578f 40%,#6c7fa9 70%,#30473a 100%)}
.hero-photo{position:absolute;left:49px;top:50px;width:650px;height:495px;background:linear-gradient(120deg,#d9d9e3 0%,#b64a55 45%,#c9b09a 62%,#1f2d56 100%)}
.hero-tagline{position:absolute;left:0;right:0;bottom:30px;text-align:center;color:var(--white);font-family:"Montserrat",Arial,sans-serif;font-weight:700;font-size:33px;line-height:1.15}
.donate-form{position:absolute;left:719px;top:50px;width:400px;height:495px;background:#eef0f4;padding:34px 29px 0}
.donate-form h2{font-size:27px;font-weight:700;text-align:center;color:#222}
.donate-form p{font-size:14px;font-weight:600;text-align:center;line-height:1.3;margin:10px 0 15px;color:#333}
.field{display:block;width:100%;height:36px;border:1px solid var(--line);border-radius:3px;background:var(--field);padding:0 16px;font:600 14px "Open Sans",Arial,sans-serif;color:#333;margin-bottom:9px}
.field::placeholder{color:#333}
.pair{display:flex;gap:9px}
.pair .field{flex:1}
.select{display:flex;justify-content:space-between;align-items:center}
.btn{display:block;margin:6px auto 0;width:164px;height:35px;background:var(--red);color:var(--white);border:0;font:700 15px "Montserrat",Arial,sans-serif}

/* sections */
.section-title{font-family:"Montserrat",Arial,sans-serif;font-weight:700;font-size:27px;color:var(--navy);text-align:center}
.how{height:379px;padding-top:24px}
.steps{display:flex;justify-content:center;gap:100px;margin-top:24px}
.step{width:190px;text-align:center;font-weight:700;font-size:16px;line-height:1.35}
.ring{width:190px;height:190px;border-radius:50%;border:2px solid var(--navy);padding:4px;margin-bottom:26px}
.ring-fill{width:100%;height:100%;border-radius:50%;background:var(--royal);display:flex;align-items:center;justify-content:center}
.ring-art{width:100px;height:84px;border-radius:10px}

.why{height:379px;background:linear-gradient(100deg,#2b3778 0%,#4a4d90 40%,#6e6aa6 70%,#3c4a8a 100%);color:var(--white);padding:38px 0 0 97px}
.why .section-title{color:var(--white);margin-left:-97px;margin-bottom:30px}
.reasons{list-style:none}
.reasons li{display:flex;align-items:center;gap:14px;font-size:15.5px;height:35px}
.reasons b{font-weight:700}
.bullet{width:26px;height:26px;flex:none}

.today{height:511px;padding-top:38px}
.perks{display:flex;justify-content:center;gap:70px;margin-top:26px}
.perk{width:140px;text-align:center;font-weight:600;font-size:16px;line-height:1.3}
.perk .ring{width:140px;height:140px;margin-bottom:16px;padding:3px}
.perk svg{width:80px;height:80px}
.secure{margin-top:44px}
.badges{display:flex;justify-content:center;align-items:center;gap:40px;margin-top:28px}
.badge-rect{width:128px;height:54px;background:#0f5c74;border:2px solid #111}
.badge-seal{width:66px;height:66px;border-radius:50%;background:#d8e6ef;border:3px solid #6fa3c4}
.badge-shield{width:124px;height:40px;display:flex;align-items:center;gap:8px}
.badge-shield span{width:36px;height:40px;background:#b71c1c;border-radius:4px 4px 18px 18px}
.badge-shield i{width:78px;height:24px;background:#444;border-radius:3px}

/* footer */
.footer{height:226px;position:relative;background:var(--navy-deep);color:var(--white);display:flex;padding:34px 0 0 67px}
.footer-flag{position:absolute;right:0;top:0;width:420px;height:226px;background:linear-gradient(105deg,var(--navy-deep) 0%,#30407a 30%,#b23a45 60%,#c8c3c8 80%,#9b2833 100%);clip-path:polygon(25% 0,100% 0,100% 100%,0 100%)}
.footer h3{font-size:14px;font-weight:700;color:#b8c6f2;margin-bottom:14px}
.footer-about{width:270px;font-size:12.5px;font-weight:600;line-height:1.45}
.footer-nav{margin-left:44px;width:140px}
.footer-nav a{display:block;color:var(--white);text-decoration:none;font-size:12.5px;font-weight:600;line-height:1.7}
.footer-contact{font-size:13px;font-weight:700;line-height:1.5;position:relative;z-index:1}
.contact-row{display:flex;gap:12px}
.footer-brand{position:absolute;right:40px;top:98px;display:flex;align-items:center;gap:10px;z-index:1}
.footer-brand .brand-dot{width:30px;height:30px}
.footer-brand .brand-name{font-size:24px}
.copyright{height:39px;display:flex;align-items:center;justify-content:center;font-size:12px;font-weight:700;color:#222}
</style>
</head>
<body>
<div class="site">
  <header class="masthead">
    <div class="brand"><span class="brand-dot"></span><span class="brand-name">Rides for Heroes</span></div>
    <div class="hotline">
      <div class="a">WE NEED YOUR HELP</div>
      <div class="b">CALL 1-800-555-0147</div>
      <div class="c">Live Operators Available</div>
      <div class="c">7 Days A Week</div>
    </div>
  </header>
  <nav class="mainnav">
    <a href="#how">HOW TO DONATE</a><a href="#why">WHY DONATE</a><a href="#faq">FAQ</a><a href="#about">ABOUT</a>
  </nav>

  <section class="hero" role="img" aria-label="Waving American flag and trees under a blue sky">
    <div class="hero-photo" role="img" aria-label="Uniformed service member saluting in front of the American flag">
      <div class="hero-tagline">DONATE YOUR CAR TO A VET,<br>MAKE A DIFFERENCE.</div>
    </div>
    <form class="donate-form">
      <h2 class="heading">DONATE YOUR CAR</h2>
      <p>Full Tax Deduction - Running or Not<br>Please fill out form or Call toll-free<br>1-800-555-0147</p>
      <input class="field" placeholder="Full Name">
      <div class="pair"><input class="field" placeholder="Daytime Phone"><input class="field" placeholder="Email"></div>
      <input class="field" placeholder="Pickup Address Line 1">
      <input class="field" placeholder="Pickup Address Line 2">
      <input class="field" placeholder="Pickup City">
      <div class="pair">
        <div class="field select">Pickup State<svg width="12" height="8" viewBox="0 0 12 8"><path d="M0 0h12L6 8z" fill="#333"/></svg></div>
        <input class="field" placeholder="Zip Code">
      </div>
      <button class="btn" type="button">DONATE NOW</button>
    </form>
  </section>

  <section class="how" id="how">
    <h2 class="section-title">HOW TO DONATE</h2>
    <div class="steps">
      <div class="step"><div class="ring"><div class="ring-fill"><div class="ring-art" role="img" aria-label="Cordless telephone illustration" style="background:linear-gradient(#e4e6ea,#8d939c)"></div></div></div>CALL US 1-800-555-0147<br>OR FILL OUT THE FORM</div>
      <div class="step"><div class="ring"><div class="ring-fill"><div class="ring-art" role="img" aria-label="Vintage tow truck illustration" style="background:linear-gradient(#5cc3c6,#1f6f73)"></div></div></div>WE TOW IT</div>
      <div class="step"><div class="ring"><div class="ring-fill"><div class="ring-art" role="img" aria-label="Paper forms and pen illustration" style="background:linear-gradient(#ffffff,#c9ccd3)"></div></div></div>TAX WRITE-OFF</div>
    </div>
  </section>

  <section class="why" id="why" role="img" aria-label="Faded American flag background">
    <h2 class="section-title">WHY DONATE YOUR CARS TO US?</h2>
    <ul class="reasons">
      <li><svg class="bullet" viewBox="0 0 26 26"><circle cx="13" cy="13" r="12" fill="#e3161d" stroke="#fff" stroke-width="1.5"/><path d="M7 13h11M14 8.5l4.5 4.5-4.5 4.5" fill="none" stroke="#fff" stroke-width="2"/></svg><span><b>TrustBoard A+ Rated &amp; IRS 501(c)3 Approved :</b> Free 24/7 Pickup with No DMV Hassles.</span></li>
      <li><svg class="bullet" viewBox="0 0 26 26"><circle cx="13" cy="13" r="12" fill="#e3161d" stroke="#fff" stroke-width="1.5"/><path d="M7 13h11M14 8.5l4.5 4.5-4.5 4.5" fill="none" stroke="#fff" stroke-width="2"/></svg><span><b>Free Local Towing :</b> We will pick up your car donation, running or not, when it's most convenient, at home or work.</span></li>
      <li><svg class="bullet" viewBox="0 0 26 26"><circle cx="13" cy="13" r="12" fill="#e3161d" stroke="#fff" stroke-width="1.5"/><path d="M7 13h11M14 8.5l4.5 4.5-4.5 4.5" fill="none" stroke="#fff" stroke-width="2"/></svg><span><b>All Cars Accepted :</b> We take your car regardless of its condition or registration status.</span></li>
      <li><svg class="bullet" viewBox="0 0 26 26"><circle cx="13" cy="13" r="12" fill="#e3161d" stroke="#fff" stroke-width="1.5"/><path d="M7 13h11M14 8.5l4.5 4.5-4.5 4.5" fill="none" stroke="#fff" stroke-width="2"/></svg><span><b>Income Tax Deduction :</b> We issue you an IRS tax receipt &amp; offer the largest resale network to get you the highest tax write-off possible.</span></li>
      <li><svg class="bullet" viewBox="0 0 26 26"><circle cx="13" cy="13" r="12" fill="#e3161d" stroke="#fff" stroke-width="1.5"/><path d="M7 13h11M14 8.5l4.5 4.5-4.5 4.5" fill="none" stroke="#fff" stroke-width="2"/></svg><span><b>No Paperwork Hassles :</b> We take any car and handle everything: DMV, Smog and IRS paperwork.</span></li>
      <li><svg class="bullet" viewBox="0 0 26 26"><circle cx="13" cy="13" r="12" fill="#e3161d" stroke="#fff" stroke-width="1.5"/><path d="M7 13h11M14 8.5l4.5 4.5-4.5 4.5" fill="none" stroke="#fff" stroke-width="2"/></svg><span><b>Car donations help fund programs :</b> And benefit Hometown Heroes Support Fund. An IRS 501(c)3 nonprofit organization.</span></li>
      <li><svg class="bullet" viewBox="0 0 26 26"><circle cx="13" cy="13" r="12" fill="#e3161d" stroke="#fff" stroke-width="1.5"/><path d="M7 13h11M14 8.5l4.5 4.5-4.5 4.5" fill="none" stroke="#fff" stroke-width="2"/></svg><span><b>Schedule a Free Pickup :</b> Complete the form and a representative will call you to arrange a convenient time to pickup your car.</span></li>
    </ul>
  </section>

  <section class="today">
    <h2 class="section-title">DONATE YOUR CAR TODAY</h2>
    <div class="perks">
      <div class="perk"><div class="ring"><div class="ring-fill">
        <svg viewBox="0 0 80 80"><path d="M68 30A30 30 0 1 1 56 14" fill="none" stroke="#fff" stroke-width="8" stroke-linecap="round"/><path d="M24 38l14 14 32-34" fill="none" stroke="#fff" stroke-width="9" stroke-linecap="round" stroke-linejoin="round"/></svg>
      </div></div>You have no costs.</div>
      <div class="perk"><div class="ring"><div class="ring-fill">
        <svg viewBox="0 0 80 80"><path d="M10 44h44V30l-14-12H30v26" fill="none" stroke="#fff" stroke-width="6" stroke-linejoin="round"/><path d="M54 44l14-24" stroke="#fff" stroke-width="6"/><path d="M68 20v14a5 5 0 1 1-6 4" fill="none" stroke="#fff" stroke-width="4"/><circle cx="20" cy="56" r="9" fill="#fff"/><circle cx="48" cy="56" r="9" fill="#fff"/></svg>
      </div></div>Free towing, running<br>or not.</div>
      <div class="perk"><div class="ring"><div class="ring-fill">
        <svg viewBox="0 0 80 80"><path d="M18 8h44v64l-7-5-8 5-7-5-8 5-7-5-7 5z" fill="none" stroke="#fff" stroke-width="5" stroke-linejoin="round"/><path d="M26 20h28M40 30v20" stroke="#fff" stroke-width="4"/><path d="M46 34h-9a4 4 0 0 0 0 8h6a4 4 0 0 1 0 8h-9" fill="none" stroke="#fff" stroke-width="3"/></svg>
      </div></div>We issue you an<br>IRS tax receipt.</div>
      <div class="perk"><div class="ring"><div class="ring-fill">
        <svg viewBox="0 0 80 80"><path d="M28 10h32v50H28z" fill="none" stroke="#fff" stroke-width="5"/><path d="M36 20h16M36 28h16" stroke="#fff" stroke-width="3"/><circle cx="32" cy="44" r="14" fill="#2d4a9a" stroke="#fff" stroke-width="5"/><path d="M32 37v9M32 50v2" stroke="#fff" stroke-width="4"/><path d="M22 55L10 68" stroke="#fff" stroke-width="7" stroke-linecap="round"/></svg>
      </div></div>We take care of<br>all paperwork.</div>
      <div class="perk"><div class="ring"><div class="ring-fill">
        <svg viewBox="0 0 80 80"><path d="M16 14h48v58H16z" fill="none" stroke="#fff" stroke-width="5"/><rect x="30" y="8" width="20" height="12" rx="3" fill="#fff"/><path d="M26 46l4-10h20l4 10v8H26z" fill="#fff"/><path d="M26 30h28M26 62h28" stroke="#fff" stroke-width="3"/></svg>
      </div></div>We take care of<br>DMV &amp; Smog issues.</div>
    </div>
    <h2 class="section-title secure">SAFE &amp; SECURE</h2>
    <div class="badges">
      <div class="badge-rect"></div>
      <div class="badge-seal"></div>
      <div class="badge-shield"><span></span><i></i></div>
    </div>
  </section>

  <footer class="footer" id="about">
    <div class="footer-flag" role="img" aria-label="Waving American flag"></div>
    <div class="footer-about">
      <h3>About Rides for Heroes</h3>
      Lorem ipsum dolor sit amet, consectetuer adipiscing elit, sed diam nonummy nibheu ismod tincidunt ut laoreet dolore magna aliquam erat volutpat. Ut wisi enim ad mini veniam, quis nostrud exerci tation ullamcor per suscipit lobortis nisl ut aliquip ex ea co modo consequat.
    </div>
    <div class="footer-nav">
      <h3>Navigation</h3>
      <a href="#how">How To Donate</a><a href="#why">Why Donate</a><a href="#faq">Faq</a><a href="#about">About</a>
    </div>
    <div class="footer-contact">
      <h3>Contact Info</h3>
      <div class="contact-row">
        <svg width="18" height="16" viewBox="0 0 18 16"><path d="M1 5c0-3 16-3 16 0v2h-4V5H5v2H1z" fill="#fff"/><path d="M4 8h10l2 7H2z" fill="#fff"/></svg>
        <div>CALL 1-800-555-0147<br>Live Operators Available<br>7 Days A Week</div>
      </div>
    </div>
    <div class="footer-brand"><span class="brand-dot"></span><span class="brand-name">Rides for Heroes</span></div>
  </footer>
  <div class="copyright">COPYRIGHT © 2016 RIDES FOR HEROES. ALL RIGHTS RESERVED.</div>
</div>
</body>
</html>
```